Business Card for Veltrano, a french tech company

Tech company
New technologies
Serious design
Dark theme

User info :
Name: Mathis CORLAVE
Position: Co-Founder & CEO
Tel: (+33) 6 58 24 90 37
Email: mathis@veltrano.io
Website: www.veltrano.io
Address: 17 rue des Tanneurs 69002 LYON

Attached is the business logo file.

```html
<!DOCTYPE html>
<html lang="fr">
<head>
<meta charset="utf-8">
<title>Veltrano — Business Card</title>
<link href="https://fonts.googleapis.com/css2?family=Roboto:wght@400;500;700;900&display=swap" rel="stylesheet">
<style>
  :root {
    --backdrop: #ababab;
    --front-start: #a5248f;
    --front-mid: #6a1872;
    --front-end: #1e0a3f;
    --back-start: #0c1549;
    --back-mid: #0a3364;
    --back-end: #0a5784;
    --ink: #ffffff;
    --ink-soft: #e8ecf4;
    --shadow: rgba(0, 0, 0, 0.35);
  }
  * { margin: 0; padding: 0; box-sizing: border-box; }
  html, body {
    width: 1200px;
    height: 1000px;
    overflow: hidden;
  }
  body {
    position: relative;
    background: var(--backdrop);
    font-family: "Roboto", Arial, sans-serif;
    color: var(--ink);
  }
  .card {
    position: absolute;
    width: 613px;
    height: 352px;
    border-radius: 24px;
    overflow: hidden;
    box-shadow: 0 24px 40px var(--shadow);
  }
  .card-front {
    left: 293px;
    top: 118px;
    background: linear-gradient(90deg, var(--front-start) 0%, var(--front-mid) 45%, var(--front-end) 100%);
  }
  .card-back {
    left: 294px;
    top: 530px;
    background: linear-gradient(90deg, var(--back-start) 0%, var(--back-mid) 50%, var(--back-end) 100%);
  }
  .wordmark {
    position: absolute;
    font-weight: 700;
    text-transform: uppercase;
    color: var(--ink);
    line-height: 1;
    white-space: nowrap;
  }
  .card-front .wordmark {
    left: 52px;
    top: 166px;
    font-size: 58px;
    letter-spacing: 1.5px;
  }
  .card-back .wordmark {
    left: 319px;
    top: 72px;
    font-size: 38px;
    letter-spacing: 1px;
  }
  .person {
    position: absolute;
    left: 49px;
    top: 163px;
    font-size: 17px;
    line-height: 22px;
  }
  .person-name { font-weight: 700; }
  .person-role { font-weight: 400; color: var(--ink-soft); }
  .contact {
    position: absolute;
    left: 319px;
    font-size: 14px;
    line-height: 17px;
    color: var(--ink-soft);
  }
  .contact-address { top: 163px; }
  .contact-lines { top: 230px; }
</style>
</head>
<body>
  <section class="card card-front" aria-label="Recto">
    <div class="wordmark">Veltrano</div>
  </section>

  <section class="card card-back" aria-label="Verso">
    <div class="wordmark">Veltrano</div>
    <div class="person">
      <p class="person-name">Mathis CORLAVE</p>
      <p class="person-role">Co-Founder &amp; CEO</p>
    </div>
    <address class="contact contact-address" style="font-style:normal">
      <p>17 rue des Tanneurs</p>
      <p>69002 LYON</p>
    </address>
    <div class="contact contact-lines">
      <p>(+33) 6 58 24 90 37</p>
      <p>mathis@veltrano.io</p>
      <p>www.veltrano.io</p>
    </div>
  </section>
</body>
</html>
```